Wix web design for healthcare IT consulting firm.

I am looking for a web design built in Wix that it will be easy for me to add or edit content in the future. The web site does not need to be overly complicated, but it should look very polished and professional. I also want to ensure it is mobile device friendly. I do not need any type of on-line purchasing ability. I will eventually do blogs, but for now it is a fairly standard web site with main page, about us, services provided, etc. I would also like a place for potential customers to contact us directly from the web site. I have included a Word document with some content for the web design. I have also included my logo and business card for reference. I would like to utilize similar colors as my business card. One of my primary competitors is https://vontalmhc.example/

Target Market(s)

Target market could be nursing home CEO, CIO, or other leader at an organization that manages long term care facilities.

Number of Pages Required

5+ page

Colors
876aae

Requirements
Must have
• Be designed to be used in Wix. Use the content I provided to create and make web design. Allow to be viewed on mobile device. Please use similar color structure as attached business card. Please use attached logo in design.

```html
<!DOCTYPE html>
<html lang="en">
<head>
<meta charset="utf-8">
<title>Leadership Team – Meridia Health Solutions</title>
<link rel="stylesheet" href="https://fonts.googleapis.com/css2?family=Montserrat:wght@400;500;600&family=Archivo+Narrow:wght@500&display=swap">
<style>
  :root{
    --purple:#7a2eb2;
    --header:#a68fc9;
    --header-dark:#8868b6;
    --logo-bg:#6f3fa3;
    --nav-bg:#f3f3f3;
    --nav-text:#7a2eb2;
    --gold:#e8c71e;
    --ink:#2b2b2b;
    --white:#ffffff;
    --placeholder:#1a1a1a;
  }
  *{margin:0;padding:0;box-sizing:border-box}
  html,body{width:1200px;height:675px;overflow:hidden;background:var(--white)}
  body{position:relative;font-family:"Montserrat",sans-serif;color:var(--ink)}
  .site-header{position:absolute;left:0;top:0;width:1200px;height:45px;background:var(--header);box-shadow:0 2px 3px rgba(0,0,0,.25)}
  .site-header__brandzone{position:absolute;left:0;top:0;width:296px;height:45px;background:var(--header-dark)}
  .brand{position:absolute;left:95px;top:0;width:161px;height:37px;background:var(--logo-bg);display:flex;align-items:center;justify-content:center;color:var(--white);font-weight:600;font-size:15px;letter-spacing:.3px}
  .main-nav{position:absolute;left:625px;top:11px;display:flex;gap:1px}
  .main-nav a{display:flex;align-items:center;justify-content:center;height:24px;background:var(--nav-bg);color:var(--nav-text);font-family:"Archivo Narrow",sans-serif;font-weight:500;font-size:12px;text-decoration:none;letter-spacing:.3px}
  .main-nav a.is-active{background:var(--purple);color:var(--white)}
  .page-title{position:absolute;left:0;top:52px;width:1256px;text-align:center;font-weight:600;font-size:40px;color:var(--purple);letter-spacing:1.5px}
  .title-rule{position:absolute;left:550px;top:127px;width:104px;height:5px;background:var(--gold)}
  .portrait{position:absolute;top:130px;width:192px;height:116px;border-radius:50%;background:linear-gradient(180deg,#3a3a3a,var(--placeholder))}
  .portrait--ceo{left:291px}
  .portrait--coo{left:719px}
  .leader-name{position:absolute;text-align:center;font-weight:600;font-size:15.5px;line-height:18.5px;letter-spacing:.8px;color:var(--ink)}
  .leader-role{position:absolute;text-align:center;font-weight:400;font-size:17px;letter-spacing:.6px;color:var(--ink)}
  .bio{position:absolute;top:366px;height:304px;border:4px solid var(--purple)}
  .bio--ceo{left:155px;width:451px}
  .bio--coo{left:607px;width:431px}
  .bio__lead,.bio__tail{position:absolute;white-space:nowrap;color:var(--ink)}
  .bio__lead{top:22px;font-size:11.8px;line-height:15.2px;letter-spacing:.75px}
  .bio__tail{top:192px;font-size:13px;line-height:17.6px;letter-spacing:.35px}
  .bio--ceo .bio__lead,.bio--ceo .bio__tail{left:17px}
  .bio--coo .bio__lead,.bio--coo .bio__tail{left:13px}
</style>
</head>
<body>
  <header class="site-header">
    <div class="site-header__brandzone"></div>
    <div class="brand">Meridia Health</div>
    <nav class="main-nav">
      <a href="#" style="width:98px">HOME</a>
      <a href="#" style="width:103px">ABOUT</a>
      <a href="#" class="is-active" style="width:121px">OUR TEAM</a>
      <a href="#" style="width:117px">SERVICES</a>
      <a href="#" style="width:117px">CONTACT</a>
    </nav>
  </header>

  <h1 class="page-title">Leadership Team</h1>
  <div class="title-rule"></div>

  <div class="portrait portrait--ceo" role="img" aria-label="Portrait of the President and CEO"></div>
  <div class="portrait portrait--coo" role="img" aria-label="Portrait of the Vice President and COO"></div>

  <p class="leader-name" style="left:235px;top:277px;width:300px">Dana Marsh, MHA, MBA,<br>CHTLX, CDHPRO</p>
  <p class="leader-role" style="left:235px;top:329px;width:265px">President and CEO</p>
  <p class="leader-name" style="left:672px;top:277px;width:300px;font-size:16.5px;line-height:19.5px">Elena Brooks,<br>BSW, MA</p>
  <p class="leader-role" style="left:672px;top:325px;width:292px">Vice President and COO</p>

  <section class="bio bio--ceo">
    <p class="bio__lead">As the Founder and CEO of Meridia HS. Dana has been<br>working in the technology industry for over 25 years with<br>extensive experience in healthcare and IT. As a consultant<br>Dana held multiple roles including CIO and CISO. Over the<br>years, Dana has been the executive sponsor of multiple<br>electronic health record (EHR) implementations. He has<br>created and nurtured numerous successful IT<br>departments and created strong relationships with<br>leadership teams. Dana strives to learn and grow as a<br>professional. He holds a Master’s in Business<br>Administration as well as a Master’s in Healthcare</p>
    <p class="bio__tail">Administration. In addition, Dana has also achieved<br>certification with both the Council of Health<br>Information Executives (CHIE) and the<br>Health Information Systems Alliance (HISA).</p>
  </section>
  <section class="bio bio--coo">
    <p class="bio__lead">As the VP and Chief Operating Officer at Meridia HS,<br>Elena is passionate about providing an excellent<br>customer experience. Elena has extensive experience<br>working in the healthcare field from medical social<br>work, hospital clinic management, hospice social<br>work, home care and hospice operations and clinical<br>management. She understands the need for<br>successful Informatics support and electronic<br>healthcare implementation. The one constant in each<br>of these areas has been the need to move the<br>organization forward by striving for process</p>
    <p class="bio__tail">improvement efforts. Elena has a Bachelor’s in Social<br>Work from Prairie State University and a<br>Master’s in Organizational Management from<br>Lakeview University in Riverton, MN.</p>
  </section>
</body>
</html>
```